Locksmith Business Cards

My father-in-law is in need of new business cards for his locksmith business and I need to impress him. Kindly help me out!

You can see the previous business card attached. It is a family run business in North Wales.

No individual names on the cards.

Key Things to Feature:
- The words "Prompt", "Local", "Reliable" (as you can see under the logo on the website)
- 24h Emergency Service
- Covering All of North Wales, the Wirral and Chester
- The color blue
- A key or a lock would be interesting (similar to the ones that come up when you google locksmith business card)

Optional (only if design includes bullet points, like the example below):
https://imgvaultexample.net/gallery/582214/77109/77109_9034417_582214_image.jpg
- Residential / Commercial / Automotive
- Alarms & Cameras
- Key Cutting & Safes

https://www.corswenydd-locksmiths.co.uk/

Industry/Entity Type

Locksmith

Contact Information for Business Card

01632 960 418
07700 900 562
corswenyddlocksmiths@mailbrook.example
Corswenydd Locksmiths, The Tan Barn, 7 Ferris Row, Llandudno LL99 4QX
www.corswenydd-locksmiths.co.uk

Requirements
Must have
• - The words "Prompt", "Local", "Reliable" (as you can see under the logo on the website)
• - 24h Emergency Service
• - Covering All of North Wales, the Wirral and Chester
Nice to have
• - A key or a lock would be interesting (similar to the ones that come up when you google locksmith business card)

```html
<!DOCTYPE html>
<html lang="en">
<head>
<meta charset="utf-8">
<title>Corswenydd Locksmiths – Business Card</title>
<link rel="stylesheet" href="https://fonts.googleapis.com/css2?family=Oswald:wght@500&family=Ubuntu:wght@400;500&display=swap">
<style>
  :root {
    --navy: #1f2a6b;
    --navy-soft: #3a4a8f;
    --paper: #ffffff;
    --backdrop: #e4e2e6;
    --ink-shadow: rgba(30, 30, 50, 0.18);
  }
  * { box-sizing: border-box; margin: 0; padding: 0; }
  html, body {
    width: 1200px; height: 900px; overflow: hidden;
    background: var(--backdrop);
  }
  .sheet {
    width: 1200px; height: 900px;
    display: flex; align-items: center; justify-content: center; gap: 50px;
  }
  .card {
    position: relative;
    width: 540px; height: 310px;
    background: var(--paper);
    box-shadow: 0 10px 28px var(--ink-shadow);
    overflow: hidden;
    font-family: "Ubuntu", sans-serif;
    color: var(--navy);
  }

  /* Back side */
  .card-back .top-band {
    position: absolute; left: 0; top: 26px;
    width: 400px; height: 42px;
    background: var(--navy);
    clip-path: polygon(0 0, 100% 0, 92% 100%, 0 100%);
  }
  .card-back .coverage {
    position: absolute; left: 0; right: 0; top: 82px;
    text-align: center;
    font-size: 15px; font-weight: 500;
  }
  .contact-list {
    position: absolute; left: 40px; top: 140px;
    list-style: none;
    display: flex; flex-direction: column; gap: 9px;
    font-size: 14px;
  }
  .contact-list li { display: flex; align-items: center; gap: 10px; white-space: nowrap; }
  .contact-list .address { font-size: 12.5px; }
  .contact-icon {
    width: 18px; height: 18px; flex: none;
    border-radius: 50%; background: var(--navy);
    display: flex; align-items: center; justify-content: center;
  }
  .contact-icon svg { width: 11px; height: 11px; }

  /* Front side */
  .brand {
    position: absolute; left: 44px; top: 62px;
    display: flex; align-items: center; gap: 18px;
  }
  .brand-mark {
    width: 74px; height: 74px; background: var(--navy); flex: none;
  }
  .brand-name {
    font-family: "Oswald", sans-serif; font-weight: 500;
    font-size: 40px; line-height: 1.02; letter-spacing: 0.5px;
    color: var(--navy); text-transform: uppercase;
  }
  .tagline {
    position: absolute; left: 140px; top: 178px;
    font-size: 19px; color: var(--navy);
    letter-spacing: 0.5px;
  }
  .emergency-band {
    position: absolute; right: 0; bottom: 44px;
    width: 330px; height: 38px;
    background: var(--navy);
    clip-path: polygon(8% 0, 100% 0, 100% 100%, 0 100%);
    color: var(--paper);
    display: flex; align-items: center; justify-content: center;
    font-size: 17px; font-weight: 500; letter-spacing: 0.3px;
  }
</style>
</head>
<body>
<main class="sheet">

  <section class="card card-back" aria-label="Business card, back">
    <div class="top-band"></div>
    <p class="coverage">Covering All of North Wales, the Wirral and Chester</p>
    <ul class="contact-list">
      <li>
        <span class="contact-icon"><svg viewBox="0 0 12 12"><rect x="3.5" y="1" width="5" height="10" rx="1" fill="#fff"/></svg></span>
        07700 900 562
      </li>
      <li>
        <span class="contact-icon"><svg viewBox="0 0 12 12"><path d="M2 2.5 4 1.5 5.5 4 4.5 5.2Q5.5 7 6.8 7.6L8 6.5 10.5 8 9.5 10Q5 10 2 4Z" fill="#fff"/></svg></span>
        01632 960 418
      </li>
      <li>
        <span class="contact-icon"><svg viewBox="0 0 12 12"><rect x="1.5" y="3" width="9" height="6.5" fill="#fff"/><path d="M1.5 3 6 6.8 10.5 3" stroke="#1f2a6b" stroke-width="1" fill="none"/></svg></span>
        corswenyddlocksmiths@mailbrook.example
      </li>
      <li class="address">
        <span class="contact-icon"><svg viewBox="0 0 12 12"><path d="M6 11 2.8 6.2A3.6 3.6 0 1 1 9.2 6.2Z" fill="#fff"/><circle cx="6" cy="4.5" r="1.3" fill="#1f2a6b"/></svg></span>
        Corswenydd Locksmiths, The Tan Barn, 7 Ferris Row, Llandudno LL99 4QX
      </li>
      <li>
        <span class="contact-icon"><svg viewBox="0 0 12 12"><g stroke="#fff" stroke-width="1" fill="none"><circle cx="6" cy="6" r="4.5"/><ellipse cx="6" cy="6" rx="2" ry="4.5"/><path d="M1.5 6h9"/></g></svg></span>
        www.corswenydd-locksmiths.co.uk
      </li>
    </ul>
  </section>

  <section class="card card-front" aria-label="Business card, front">
    <div class="brand">
      <span class="brand-mark"></span>
      <h1 class="brand-name">Corswenydd<br>Locksmiths</h1>
    </div>
    <p class="tagline">Prompt • Local • Reliable</p>
    <div class="emergency-band">24h Emergency Service</div>
  </section>

</main>
</body>
</html>
```